UI improvement for an existing app

Hi, we have a mobile preorder app that was built with standard flutter UI.

Looking at improving the whole look and feel of our app and make it look more slick and on trend. Something similar to fennoplate, Quorvalo or something along these lines.

Keeping in mind that we are white labeling our app so it needs to be easily redline for other clients.

For our first client I've attached their branding guideline in this project as well.

Please find all the existing screen of our app which we are looking to improve.

Main focus is to give the app a modern and fresh look while making it easy to realign. Do ensure user experience and how they navigate the app is important

Feel free to let me know if you have any questions.

Thanks
KT

Need extra days to review

• All the functionality layout on the screenshot. There's some element that we would like to incorporate such as

1. Coupon code in checkout screen
2. Allow users to edit their profile in profile page

```html
<!DOCTYPE html>
<html lang="en">
<head>
<meta charset="utf-8">
<title>Preorder App — Home and Drinks Screens</title>
<link href="https://fonts.googleapis.com/css2?family=Ubuntu:wght@500;700&family=Noto+Sans:wght@400;600&family=Open+Sans:wght@400&display=swap" rel="stylesheet">
<style>
  :root {
    --page-bg: #e2e2e2;
    --screen-bg: #ffffff;
    --field-bg: #f7f7f7;
    --card-bg: #f8f8f8;
    --ink: #0d0d0d;
    --muted: #9a9a9a;
    --brand: #7cb83e;
    --arrow: #b9b9b9;
    --on-brand: #ffffff;
  }
  * { box-sizing: border-box; margin: 0; padding: 0; }
  html, body { width: 1200px; height: 1200px; overflow: hidden; background: var(--page-bg); }
  .screen {
    position: absolute; top: 60px; width: 499px; height: 1080px;
    background: var(--screen-bg); overflow: hidden;
  }
  .screen--home { left: 60px; }
  .screen--drinks { left: 641px; }

  .page-title {
    position: absolute; left: 32px; font-family: "Ubuntu", sans-serif; font-weight: 700;
    color: var(--ink); font-size: 31px; line-height: 50px;
  }
  .section-title {
    position: absolute; left: 32px; font-family: "Ubuntu", sans-serif; font-weight: 500;
    color: var(--ink); font-size: 25px;
  }
  .search {
    position: absolute; left: 13px; width: 472px; height: 66px; border-radius: 33px;
    background: var(--field-bg); display: flex; align-items: center; padding: 0 22px;
  }
  .search__icon { width: 24px; height: 24px; }
  .search__text {
    flex: 1; margin-left: 11px; font-family: "Open Sans", sans-serif; font-size: 15px; color: var(--muted);
  }
  .search__filter { width: 26px; height: 22px; }

  .carousel-arrow {
    position: absolute; width: 35px; height: 35px; margin: -17px 0 0 -17px; border-radius: 50%;
    background: var(--arrow); display: flex; align-items: center; justify-content: center;
  }
  .carousel-arrow svg { width: 14px; height: 14px; }

  .cup {
    position: absolute; width: 80px; clip-path: polygon(0 4%, 100% 4%, 88% 100%, 12% 100%);
    border-radius: 6px;
  }
  .cup--citrus { background: linear-gradient(180deg, #fbd14a, #f5a222 45%, #ec7f16); }
  .cup--black-tea { background: linear-gradient(180deg, #d88a3c, #b8531c 50%, #3e2418); }
  .cup--milk-jelly { background: linear-gradient(180deg, #2a2a2a 0 8%, #efece5 18%, #e9e3d6 75%, #1e1e1e); }
  .cup--milk-tea { background: linear-gradient(180deg, #2b2320 0 14%, #d8a585 26%, #e1b89c); }
  .cup--berry { background: linear-gradient(180deg, #f6e8ea 0 6%, #e3234c 14%, #c2123a); }
  .cup--summer { background: linear-gradient(180deg, #f5f0d8, #f3e07a 40%, #ecc42d); }
  .cup--passion { background: linear-gradient(180deg, #3a2a1f 0 7%, #f6b42a 20%, #ee8a17); }
  .cup--peach { background: linear-gradient(180deg, #f9e6b8, #f7d98c); }
  .cup--mango { background: linear-gradient(180deg, #f9c24a, #f2a42a); }

  .near-photo {
    position: absolute; top: 892px; height: 160px; border-radius: 25px 25px 0 0;
  }
  .near-photo--interior { left: 32px; width: 276px; background: linear-gradient(135deg, #eef2e6, #b9d36f 55%, #7f9a55); }
  .near-photo--storefront { left: 336px; width: 200px; background: linear-gradient(90deg, #9a4a35 0 28%, #f1f1ef 28%, #dcdcd6); }

  .tab-bar {
    position: absolute; left: 0; top: 992px; width: 499px; height: 88px;
    background: var(--brand); border-radius: 37px 37px 0 0;
  }
  .tab-bar svg { position: absolute; top: 22px; width: 40px; height: 40px; }

  .drink-list { position: absolute; left: 0; top: 176px; width: 499px; height: 816px; overflow: hidden; }
  .drink-card {
    position: absolute; width: 204px; border-radius: 28px; background: var(--card-bg);
  }
  .drink-card .cup { left: 64px; width: 76px; }
  .drink-card__name {
    position: absolute; left: 12px; font-family: "Noto Sans", sans-serif; font-weight: 600;
    font-size: 19.5px; color: var(--ink); white-space: nowrap; letter-spacing: 0.3px;
  }
  .drink-card__type {
    position: absolute; left: 12px; font-family: "Noto Sans", sans-serif; font-weight: 400;
    font-size: 18px; color: var(--ink); white-space: nowrap; letter-spacing: 0.4px;
  }
</style>
</head>
<body>

<svg width="0" height="0" style="position:absolute">
  <defs>
    <symbol id="icon-search" viewBox="0 0 24 24"><circle cx="10" cy="10" r="7" fill="none" stroke="#9a9a9a" stroke-width="2.2"/><line x1="15" y1="15" x2="22" y2="22" stroke="#9a9a9a" stroke-width="2.4" stroke-linecap="round"/></symbol>
    <symbol id="icon-filter" viewBox="0 0 26 22"><g stroke="#111" stroke-width="2.6" stroke-linecap="round"><line x1="1" y1="3" x2="25" y2="3"/><line x1="6" y1="11" x2="20" y2="11"/><line x1="10" y1="19" x2="16" y2="19"/></g></symbol>
    <symbol id="icon-prev" viewBox="0 0 14 14"><polyline points="9,2 4,7 9,12" fill="none" stroke="#fff" stroke-width="2.4" stroke-linecap="round" stroke-linejoin="round"/></symbol>
    <symbol id="icon-next" viewBox="0 0 14 14"><polyline points="5,2 10,7 5,12" fill="none" stroke="#fff" stroke-width="2.4" stroke-linecap="round" stroke-linejoin="round"/></symbol>
    <symbol id="icon-home" viewBox="0 0 40 40"><path d="M20 4 L2 20 H8 V36 H17 V26 H23 V36 H32 V20 H38 Z" fill="#fff"/></symbol>
    <symbol id="icon-cup" viewBox="0 0 40 40"><path d="M9 3 H31 L28 37 H12 Z" fill="#fff"/><rect x="11" y="8" width="18" height="4" fill="#7cb83e"/><rect x="13" y="31" width="14" height="3" fill="#7cb83e"/></symbol>
    <symbol id="icon-locate" viewBox="0 0 40 40"><circle cx="20" cy="20" r="12" fill="none" stroke="#fff" stroke-width="3.5"/><circle cx="20" cy="20" r="6" fill="#fff"/><g stroke="#fff" stroke-width="3.5"><line x1="20" y1="2" x2="20" y2="9"/><line x1="20" y1="31" x2="20" y2="38"/><line x1="2" y1="20" x2="9" y2="20"/><line x1="31" y1="20" x2="38" y2="20"/></g></symbol>
    <symbol id="icon-cart" viewBox="0 0 40 40"><path d="M2 5 H8 L10 10 H37 L31 24 H13 L11 28 H33" fill="none" stroke="#fff" stroke-width="3.5" stroke-linejoin="round"/><path d="M10 10 H37 L31 24 H13 Z" fill="#fff"/><circle cx="14" cy="34" r="3.5" fill="#fff"/><circle cx="30" cy="34" r="3.5" fill="#fff"/></symbol>
    <symbol id="icon-profile" viewBox="0 0 40 40"><circle cx="20" cy="20" r="19" fill="#fff"/><circle cx="20" cy="15" r="6.5" fill="#7cb83e"/><path d="M8 31 C11 23 29 23 32 31 Z" fill="#7cb83e"/></symbol>
  </defs>
</svg>

<main class="screen screen--home">
  <h1 class="page-title" style="top:30px">What would you like to<br>have today?</h1>

  <div class="search" style="top:141px">
    <svg class="search__icon"><use href="#icon-search"/></svg>
    <span class="search__text">Find your Refreshment or Location</span>
    <svg class="search__filter"><use href="#icon-filter"/></svg>
  </div>

  <h2 class="section-title" style="top:245px">Top Featured</h2>
  <div class="cup cup--citrus" role="img" aria-label="Citrus fruit tea in branded cup" style="left:74px;top:303px;height:190px"></div>
  <div class="cup cup--black-tea" role="img" aria-label="Black tea with jelly in branded cup" style="left:215px;top:305px;height:186px"></div>
  <div class="cup cup--milk-jelly" role="img" aria-label="Milk drink with dark jelly in branded cup" style="left:350px;top:308px;height:186px"></div>
  <div class="carousel-arrow" style="left:38px;top:404px"><svg><use href="#icon-prev"/></svg></div>
  <div class="carousel-arrow" style="left:463px;top:404px"><svg><use href="#icon-next"/></svg></div>

  <h2 class="section-title" style="top:541px">My Favorites</h2>
  <div class="cup cup--citrus" role="img" aria-label="Citrus fruit tea in branded cup" style="left:78px;top:597px;height:190px"></div>
  <div class="cup cup--milk-jelly" role="img" aria-label="Milk drink with dark jelly in branded cup" style="left:210px;top:603px;height:186px"></div>
  <div class="cup cup--milk-tea" role="img" aria-label="Milk tea with tapioca pearls in branded cup" style="left:345px;top:603px;height:190px"></div>
  <div class="carousel-arrow" style="left:38px;top:694px"><svg><use href="#icon-prev"/></svg></div>
  <div class="carousel-arrow" style="left:463px;top:694px"><svg><use href="#icon-next"/></svg></div>

  <h2 class="section-title" style="top:838px">Near Me</h2>
  <div class="near-photo near-photo--interior" role="img" aria-label="Photo of a tea shop interior with green walls"></div>
  <div class="near-photo near-photo--storefront" role="img" aria-label="Photo of a tea shop storefront on a brick building"></div>

  <nav class="tab-bar">
    <svg style="left:47px"><use href="#icon-home"/></svg>
    <svg style="left:136px"><use href="#icon-cup"/></svg>
    <svg style="left:224px"><use href="#icon-locate"/></svg>
    <svg style="left:319px"><use href="#icon-cart"/></svg>
    <svg style="left:417px"><use href="#icon-profile"/></svg>
  </nav>
</main>

<main class="screen screen--drinks">
  <h1 class="page-title" style="top:43px;font-size:32px">Drinks</h1>

  <div class="search" style="top:103px;width:471px;height:64px">
    <svg class="search__icon"><use href="#icon-search"/></svg>
    <span class="search__text">Find your Drink</span>
    <svg class="search__filter"><use href="#icon-filter"/></svg>
  </div>

  <section class="drink-list">
    <article class="drink-card" style="left:265px;top:-154px;height:275px">
      <div class="cup cup--peach" role="img" aria-label="Peach oolong tea in branded cup" style="top:90px;height:94px;left:82px;width:40px"></div>
      <h3 class="drink-card__name" style="top:205px">Peach Ooolong Tea</h3>
      <p class="drink-card__type" style="top:230px">Fruity Refreshment</p>
    </article>

    <article class="drink-card" style="left:29px;top:43px;height:275px">
      <div class="cup cup--citrus" role="img" aria-label="Signature fruit tea in branded cup" style="top:19px;height:170px"></div>
      <h3 class="drink-card__name" style="top:204px">Signature Fruit Tea</h3>
      <p class="drink-card__type" style="top:229px">Fruity Refreshment</p>
    </article>

    <article class="drink-card" style="left:265px;top:148px;height:276px">
      <div class="cup cup--summer" role="img" aria-label="Summer fruit tea in branded cup" style="top:36px;height:152px"></div>
      <h3 class="drink-card__name" style="top:205px">Summer Fruit Tea</h3>
      <p class="drink-card__type" style="top:230px">Fruity Refreshment</p>
    </article>

    <article class="drink-card" style="left:29px;top:345px;height:276px">
      <div class="cup cup--berry" role="img" aria-label="Blueberry fruit tea in branded cup" style="top:48px;height:136px;left:70px;width:66px"></div>
      <h3 class="drink-card__name" style="top:205px">Blueberry Fruit Tea</h3>
      <p class="drink-card__type" style="top:230px">Fruity Refreshment</p>
    </article>

    <article class="drink-card" style="left:265px;top:450px;height:275px">
      <div class="cup cup--passion" role="img" aria-label="Passionfruit drink with jelly in branded cup" style="top:33px;height:153px;left:68px;width:70px"></div>
      <h3 class="drink-card__name" style="top:204px">Passionfruit QQ</h3>
      <p class="drink-card__type" style="top:229px">Fruity Refreshment</p>
    </article>

    <article class="drink-card" style="left:29px;top:647px;height:300px">
      <div class="cup cup--mango" role="img" aria-label="Mango fruit tea in branded cup" style="top:40px;height:170px;left:66px;width:70px"></div>
    </article>

    <article class="drink-card" style="left:265px;top:752px;height:250px">
      <div class="cup cup--citrus" role="img" aria-label="Lemon fruit tea in branded cup" style="top:30px;height:170px;left:68px;width:68px"></div>
    </article>
  </section>

  <nav class="tab-bar">
    <svg style="left:47px"><use href="#icon-home"/></svg>
    <svg style="left:136px"><use href="#icon-cup"/></svg>
    <svg style="left:224px"><use href="#icon-locate"/></svg>
    <svg style="left:319px"><use href="#icon-cart"/></svg>
    <svg style="left:417px"><use href="#icon-profile"/></svg>
  </nav>
</main>

</body>
</html>
```